Moving Company Website

We need a webdesign for an established moving company in the Bay Area. We have chosen a wordpress template (see attached) and would like to revamp the design to give it a touch and feel of a leading moving company.
The design should be inspired by the following companies:
http://www.brightvanline.com/
http://www.kpcarriers.com/
Updates

The design should be based on the following WordPress template:

http://www.layoutforge.com/demo/35782.html

And based on the image I have attached.

We will get the template PSD after we will choose a designer.

Thanks
Marcus 

Industry/Entity Type

Moving Company

Requirements
Must have
• Request a quote form must be implemented in all pages
inner pages with destinations

```html
<!DOCTYPE html>
<html lang="en">
<head>
<meta charset="utf-8">
<title>Brightpath Movers</title>
<link rel="stylesheet" href="https://fonts.googleapis.com/css2?family=Oswald:wght@400;500&family=Open+Sans:ital,wght@0,400;1,400&display=swap">
<style>
:root{
  --green:#0f9447;
  --ink:#1d1d1d;
  --muted:#8a8a8a;
  --body:#555;
  --band:#f1f1f1;
  --white:#fff;
}
*{box-sizing:border-box;margin:0;padding:0}
html,body{width:759px;height:1200px;overflow:hidden;background:var(--white)}
body{font-family:"Open Sans",Arial,sans-serif;color:var(--body)}
.page{position:relative;width:759px;height:1200px;overflow:hidden}
.abs{position:absolute}
.display{font-family:"Oswald","Arial Narrow",sans-serif;text-transform:uppercase}

/* header */
.brand{left:50px;top:28px;width:94px;font-family:"Oswald",sans-serif;font-weight:500;font-size:16px;line-height:17px;color:var(--ink);text-transform:uppercase;text-align:center}
.brand-mark{display:block;width:22px;height:22px;border-radius:50%;background:var(--ink);margin:0 auto 4px}
.social{left:576px;top:17px;font-size:13px;font-weight:500;color:var(--ink);display:flex;align-items:center;gap:5px}
.social i{display:inline-block;width:11px;height:11px;border-radius:50%;background:#ddd;border:1px solid #ccc}
.rule{border-top:1px dotted #aaa}
.nav{display:flex;font-size:12.5px;color:#999;align-items:center;white-space:nowrap}
.nav a{color:inherit;text-decoration:none;padding:0 5px;border-left:1px solid #ddd;line-height:11px}
.nav a:first-child{border-left:0;padding-left:0}
.nav a:last-child{padding-right:0}
.nav a.current{color:var(--ink);text-decoration:underline;text-underline-offset:3px}
.live-chat{left:726px;top:52px;width:33px;height:75px;background:var(--green);color:var(--white);font-family:"Oswald",sans-serif;font-size:12px;display:grid;grid-template-columns:1fr 1fr;grid-template-rows:repeat(4,1fr);padding:4px;text-align:center}

/* hero */
.hero{left:41px;top:92px;width:484px;height:294px;background:linear-gradient(180deg,#2f5f95 0%,#7ea6cf 40%,#c4c7c6 62%,#6e6a66 80%,#3c3a38 100%)}
.slide-text{left:55px;top:362px;color:var(--white);font-size:14px;letter-spacing:.3px}
.slide-dots{left:464px;top:361px;width:57px;height:21px;background:#111;border-radius:3px;display:flex;gap:4px;align-items:center;justify-content:center}
.slide-dots i{width:9px;height:9px;border-radius:50%;background:var(--white)}
.slide-dots i:first-child{background:#777}

/* quote */
.quote{left:532px;top:92px;width:188px;height:294px;background:linear-gradient(180deg,#a9a9a9,#7d7d7d)}
.quote h2{position:absolute;top:16px;width:100%;text-align:center;font-weight:400;font-size:16px;color:#222}
.quote .field{position:absolute;left:13px;width:164px;height:18px;background:var(--white);font-size:8.5px;color:#888;padding:2px 5px;line-height:14px;white-space:nowrap;overflow:hidden}
.quote .select{padding-right:20px;text-align:center}
.quote .select b{position:absolute;right:0;top:0;width:19px;height:18px;background:#ddd;border-left:1px solid #bbb}
.quote .select b::after{content:"";position:absolute;left:5px;top:6px;border:4px solid transparent;border-top:6px solid #333}
.quote .submit{position:absolute;left:64px;top:230px;width:57px;height:22px;background:var(--green);color:var(--white);font-family:"Oswald",sans-serif;font-size:13px;text-align:center;line-height:22px}

/* feature columns */
.feature{top:400px;width:158px}
.feature h3{font-weight:400;font-size:23px;color:var(--ink);line-height:32px}
.feature h3.accent{color:var(--green)}
.thumb{margin-top:6px;width:157px;height:111px;border:3px solid var(--white);box-shadow:0 0 3px rgba(0,0,0,.45)}
.feature p{margin:22px 0 0 6px;width:150px;font-size:8.3px;line-height:11.8px;text-align:justify}
.more{font-family:"Oswald",sans-serif;font-size:12px;color:var(--ink);display:flex;align-items:center;gap:5px;text-decoration:none}
.more i{display:inline-block;width:12px;height:12px;border-radius:50%;background:#bdbdbd;position:relative}
.more i::after{content:"";position:absolute;left:4px;top:3px;border:3px solid transparent;border-left:4px solid var(--white)}
.more.accent{color:var(--green)}
.more.accent i{background:#7fcf91}

/* why */
.why-title{left:46px;top:712px;font-size:34px;line-height:44px;color:var(--green);font-weight:500}
.why-lead{left:64px;top:763px;width:650px;font-size:18px;line-height:27px;color:var(--muted);font-weight:400}
.why-copy{top:829px;width:300px;font-size:9.8px;line-height:13.8px;color:#777;text-align:justify}

/* lower band */
.band{left:0;top:925px;width:759px;height:200px;background:var(--band)}
.band-title{top:945px;font-weight:400;font-size:21px;line-height:28px;color:var(--ink)}
.band-title.accent{color:var(--green)}
.about{left:41px;top:977px;width:140px;font-size:8.4px;line-height:12px;text-align:justify}
.link-list{left:221px;top:978px;list-style:none;font-size:8.4px;line-height:17.6px}
.link-list li::before{content:"→";color:#888;margin-right:6px}
.link-list li span{text-decoration:underline}
.testimonial{left:399px;top:980px;width:152px;height:76px;background:var(--white);border:1px solid #ccc;border-radius:3px;padding:6px;font-size:8.4px;line-height:12px;font-style:italic;text-align:justify}
.testimonial::after{content:"";position:absolute;left:20px;bottom:-7px;width:11px;height:11px;background:var(--white);border-right:1px solid #ccc;border-bottom:1px solid #ccc;transform:rotate(45deg)}
.author{left:402px;top:1074px;font-size:8.4px;font-style:italic}
.mgmt{left:577px;top:978px;list-style:none;font-size:8.4px;line-height:12px;width:145px}
.mgmt li{position:relative;padding-left:13px;margin-bottom:11px}
.mgmt li::before{content:"";position:absolute;left:0;top:2px;width:8px;height:8px;border:1px solid #888;border-radius:50%}

/* footer */
.footer{left:0;top:1127px;width:759px;height:73px;background:linear-gradient(180deg,#e4e4e4,#f7f7f7);border-top:1px solid #ccc}
.footer-brand{left:44px;top:1140px;width:72px;font-size:12px;line-height:13px}
.copyright{left:121px;top:1159px;font-size:9px;color:#444}
</style>
</head>
<body>
<div class="page">

  <header>
    <div class="abs brand"><span class="brand-mark"></span>Brightpath Movers</div>
    <div class="abs social display">Socialize with us : <i></i><i></i><i></i></div>
    <div class="abs rule" style="left:322px;top:52px;width:398px"></div>
    <nav class="abs nav display" style="left:334px;top:64px">
      <a class="current" href="#">Home</a><a href="#">About us</a><a href="#">Services</a><a href="#">Products</a><a href="#">Partners</a><a href="#">News</a><a href="#">Contact us</a>
    </nav>
    <div class="abs live-chat"><span>L</span><span>C</span><span>I</span><span>H</span><span>V</span><span>A</span><span>E</span><span>T</span></div>
  </header>

  <section>
    <div class="abs hero" role="img" aria-label="Red moving truck with a silver trailer on a highway under a blue sky"></div>
    <div class="abs slide-text display">Slide text comes here.</div>
    <div class="abs slide-dots"><i></i><i></i><i></i></div>

    <form class="abs quote">
      <h2 class="display">Request a quote</h2>
      <div class="field" style="top:47px">Enter Your Name</div>
      <div class="field" style="top:76px">Enter Your Email Address</div>
      <div class="field" style="top:107px">Enter Your Phone Number</div>
      <div class="field" style="top:137px">From which location</div>
      <div class="field" style="top:167px">To where</div>
      <div class="field select" style="top:197px">-----------Select Service-------------<b></b></div>
      <div class="submit">GET IT</div>
    </form>
  </section>

  <section>
    <div class="abs feature" style="left:41px">
      <h3 class="display accent">Moving</h3>
      <div class="thumb" role="img" aria-label="Movers carrying furniture out of a house" style="background:linear-gradient(135deg,#6f8a5a,#9b7a55 55%,#4e3a2c)"></div>
      <p>Lorem ipsum dolor sit amet, con tuer adipiscing elitaeesent ves tibulumie lacus. Aenean my hendrerit is. Phasellus porta. Fusce suscipit varius mi. Cum sociis natoque penatibus et magnis dis parturient montes, nascetur ridiculus mus.</p>
    </div>
    <div class="abs feature" style="left:214px">
      <h3 class="display">Storage</h3>
      <div class="thumb" role="img" aria-label="Warehouse interior with stacked cardboard boxes" style="background:linear-gradient(180deg,#7d8a96,#b8b6ae 55%,#c4a778)"></div>
      <p>Lorem ipsum dolor sit amet, con tuer adipiscing elitaeesent ves tibulumie lacus. Aenean my hendrerit is. Phasellus porta. Fusce suscipit varius mi. Cum sociis natoque penatibus et magnis dis parturient montes, nascetur ridiculus mus.</p>
    </div>
    <div class="abs feature" style="left:388px">
      <h3 class="display">Services</h3>
      <div class="thumb" role="img" aria-label="Mover in overalls carrying a cardboard box" style="background:linear-gradient(135deg,#e6ddcf,#c9a472 55%,#3e5f8f)"></div>
      <p>Lorem ipsum dolor sit amet, con tuer adipiscing elitaeesent ves tibulumie lacus. Aenean my hendrerit is. Phasellus porta. Fusce suscipit varius mi. Cum sociis natoque penatibus et magnis dis parturient montes, nascetur ridiculus mus.</p>
    </div>
    <div class="abs feature" style="left:561px">
      <h3 class="display">Videos</h3>
      <div class="thumb" role="img" aria-label="Video still of movers loading furniture" style="background:linear-gradient(135deg,#5d6b4c,#8a6d50 55%,#3d3029);position:relative">
        <svg width="151" height="105" viewBox="0 0 151 105" style="position:absolute;left:0;top:0"><circle cx="76" cy="52" r="23" fill="#333" fill-opacity=".7" stroke="#fff" stroke-width="2.5"/><path d="M69 40 L88 52 L69 64 Z" fill="#fff"/></svg>
      </div>
      <p>Lorem ipsum dolor sit amet, con tuer adipiscing elitaeesent ves tibulumie lacus. Aenean my hendrerit is. Phasellus porta. Fusce suscipit varius mi. Cum sociis natoque penatibus et magnis dis parturient montes, nascetur ridiculus mus.</p>
    </div>
    <a class="abs more accent" href="#" style="left:47px;top:668px">more info <i></i></a>
    <a class="abs more" href="#" style="left:220px;top:668px">more info <i></i></a>
    <a class="abs more" href="#" style="left:393px;top:668px">more info <i></i></a>
    <a class="abs more" href="#" style="left:566px;top:668px">more info <i></i></a>
    <div class="abs rule" style="left:41px;top:703px;width:677px"></div>
  </section>

  <section>
    <h2 class="abs why-title display">Why us?</h2>
    <p class="abs why-lead display">We are devoted to your satisfaction and take a great deal of pride in our work. Every specialist in our team is thoroughly trained and ready to help.</p>
    <p class="abs why-copy" style="left:64px">Lorem ipsum dolor sit amet, con tuer adipiscing elitaeesent ves tibulumie lacus. Aenean my hendrerit is. Phasellus porta. Fusce suscipit varius mi. Cum sociis natoque penatibus et magnis dis parturient montes, nascetur ridiculus mus. Nulla dui. Fusce feugiat malesuada odio. Morbi nunc odio gravida at cursus nec</p>
    <p class="abs why-copy" style="left:388px">Lorem ipsum dolor sit amet, con tuer adipiscing elitaeesent ves tibulumie lacus. Aenean my hendrerit is. Phasellus porta. Fusce suscipit varius mi. Cum sociis natoque penatibus et magnis dis parturient montes, nascetur ridiculus mus. Nulla dui. Fusce feugiat malesuada odio. Morbi nunc odio gravida at cursus nec</p>
  </section>

  <section>
    <div class="abs band"></div>
    <h3 class="abs band-title display accent" style="left:39px">About us</h3>
    <h3 class="abs band-title display" style="left:220px">Research</h3>
    <h3 class="abs band-title display" style="left:398px">Testimonials</h3>
    <h3 class="abs band-title display" style="left:578px">Management</h3>

    <p class="abs about">Lorem ipsum dolor sit amet, con tuer adipiscing elitaeesent ves tibulumie lacus. Aenean my hendrerit is. Phasellus porta. Fusce suscipit varius mi. Cum sociis natoque penatibus et magnis dis parturient montes, nascetur ridiculus mus.</p>

    <ul class="abs link-list">
      <li><span>Lorem ipsum dolor sit amet,</span></li>
      <li><span>Con tuer adipiscing elitaesent.</span></li>
      <li><span>Aenean my hendrerit is.</span></li>
      <li><span>Fusce suscipit varius mi.</span></li>
      <li><span>Con tuer adipiscing elitaesent.</span></li>
      <li><span>Aenean my hendrerit is.</span></li>
    </ul>

    <blockquote class="abs testimonial">Lorem ipsum dolor sit amet, con tuer adipiscing elitaeesent ves tibulumie lacus. Aenean my hendrerit is. Phasellus porta. Fusce suscipit varius mi. Cum sociis</blockquote>
    <div class="abs author">Sam Porter, Manager</div>

    <ul class="abs mgmt">
      <li>Lorem ipsum dolor sit amet,</li>
      <li>con tuer adipiscing elitaeesent ves tibulumie lacus.</li>
      <li>Aenean my hendrerit is. Phasellus porta.</li>
      <li>Fusce suscipit varius mi.</li>
    </ul>

    <a class="abs more accent" href="#" style="left:44px;top:1093px">more info <i></i></a>
    <a class="abs more" href="#" style="left:221px;top:1093px">more info <i></i></a>
    <a class="abs more" href="#" style="left:401px;top:1093px">more info <i></i></a>
    <a class="abs more" href="#" style="left:580px;top:1093px">more info <i></i></a>
  </section>

  <footer>
    <div class="abs footer"></div>
    <div class="abs brand footer-brand"><span class="brand-mark" style="width:16px;height:16px"></span>Brightpath Movers</div>
    <div class="abs copyright">© 2012.&nbsp; Privacy Policy</div>
    <nav class="abs nav display" style="left:334px;top:1157px">
      <a class="current" href="#" style="text-decoration:none">Home</a><a href="#">About us</a><a href="#">Services</a><a href="#">Products</a><a href="#">Partners</a><a href="#">News</a><a href="#">Contact us</a>
    </nav>
  </footer>

</div>
</body>
</html>
```